Dental Practice Billboard Design

We are a newer dental practice in need of a simple but appealing billboard for our growing dental practice to attract new patients. The practice is owned by husband and wife dentists and is family friendly in a small town in Kentucky. We try to be very friendly and caring to our patients. Would prefer a blue background for the billboard and our tooth logo to be prominent. We are partial to the Patua One font used in the image below but please feel free to tweak it as you deem necessary. The shape of the uppercase D and lowercase g are why we like that font, so fonts with a similarly shaped “D” and “g” would work as well. Please include our phone number (606) 847-3962. Please see our website Harlowfamilydentistry.com for more info on the practice if needed. Thank you! Looking forward to seeing your creation.
Updates

The dimensions will be 12ft x 24ft (3.6576m x 7.3152m). Apologies for not including this in the original prompt. Thank you all for your submissions.

Industry/Entity Type

Dental

Font styles to use
Other font styles liked:
• Patua One

Colors
0054AA
0677BA
7BADD7
CADEEF
E8F1F8
0094D4
00A9DD
6FCCEA
C7EBF8
E9F6FB
00AB8E
00BBA5
67D7C9
C6EFE9
E9F9F6
59FF00
82FF00
B8FF75
E3FFCB
F4FFEA

Requirements
Must have
• Phone number, website, Logo, Practice name “Harlow Family Dentistry”
Should not have
• A tagline or slogan

```html
<!DOCTYPE html>
<html lang="en">
<head>
<meta charset="utf-8">
<title>Harlow Family Dentistry – Billboard</title>
<link rel="stylesheet" href="https://fonts.googleapis.com/css2?family=Patua+One&display=swap">
<style>
  :root {
    --page-bg: #ffffff;
    --board-top: #2557a4;
    --board-bottom: #1b2d63;
    --band-light: #22489a;
    --band-dark: #1a2c62;
    --brand-green: #3bb54a;
    --text-white: #ffffff;
    --url-ink: #1d3170;
  }
  * { box-sizing: border-box; margin: 0; padding: 0; }
  html, body {
    width: 1200px;
    height: 1062px;
    overflow: hidden;
    background: var(--page-bg);
  }
  .billboard {
    position: absolute;
    left: 40px;
    top: 368px;
    width: 1120px;
    height: 325px;
    background: linear-gradient(180deg, var(--board-top) 0%, var(--board-bottom) 100%);
    box-shadow: 0 4px 10px rgba(0,0,0,0.35);
    font-family: "Patua One", Georgia, serif;
    overflow: hidden;
  }
  .headline {
    position: absolute;
    left: 27px;
    top: 22px;
    font-size: 68px;
    line-height: 70px;
    font-weight: 400;
    letter-spacing: 0.5px;
  }
  .headline .line-top { color: var(--text-white); display: block; }
  .headline .line-bottom { color: var(--brand-green); display: block; }
  .brand {
    position: absolute;
    left: 712px;
    top: 34px;
    display: flex;
    align-items: center;
    gap: 24px;
  }
  .brand-dot {
    width: 108px;
    height: 108px;
    border-radius: 50%;
    background: var(--brand-green);
    flex: none;
  }
  .brand-name {
    color: var(--text-white);
    text-align: right;
    line-height: 1;
  }
  .brand-name .name-main { display: block; font-size: 70px; line-height: 76px; }
  .brand-name .name-sub { display: block; font-size: 31px; line-height: 38px; }
  .contact-band {
    position: absolute;
    left: 0;
    top: 204px;
    width: 100%;
    height: 76px;
    background: linear-gradient(90deg, var(--band-dark) 0%, var(--band-light) 12%, var(--band-light) 88%, var(--band-dark) 100%);
  }
  .phone {
    position: absolute;
    left: 127px;
    top: 214px;
    display: flex;
    align-items: center;
    gap: 10px;
    color: var(--text-white);
    font-size: 52px;
    line-height: 56px;
  }
  .phone-icon { width: 48px; height: 48px; flex: none; }
  .website {
    position: absolute;
    left: 549px;
    top: 220px;
    width: 443px;
    height: 43px;
    border-radius: 5px;
    background: var(--brand-green);
    color: var(--url-ink);
    font-size: 23px;
    line-height: 43px;
    text-align: center;
  }
  .base-stripe {
    position: absolute;
    left: 0;
    bottom: 0;
    width: 100%;
    height: 10px;
    background: var(--brand-green);
  }
</style>
</head>
<body>
  <section class="billboard" aria-label="Harlow Family Dentistry billboard">
    <h1 class="headline">
      <span class="line-top">NOW ACCEPTING</span>
      <span class="line-bottom">NEW PATIENTS</span>
    </h1>

    <div class="brand">
      <span class="brand-dot" aria-hidden="true"></span>
      <p class="brand-name">
        <span class="name-main">Harlow</span>
        <span class="name-sub">Family Dentistry</span>
      </p>
    </div>

    <div class="contact-band" aria-hidden="true"></div>

    <p class="phone">
      <svg class="phone-icon" viewBox="0 0 48 48" aria-hidden="true">
        <path fill="#3bb54a" d="M11 5c2-1 4 0 5 2l4 8c1 2 0 4-1 5l-3 3c2 5 6 9 11 11l3-3c1-1 3-2 5-1l8 4c2 1 3 3 2 5l-2 4c-1 2-3 3-6 3C20 45 3 28 3 11c0-3 1-5 3-6z"/>
        <path fill="none" stroke="#3bb54a" stroke-width="3.5" stroke-linecap="round" stroke-linejoin="round" d="M27 21L40 8M31 8h9v9"/>
      </svg>
      <span>(606) 847-3962</span>
    </p>

    <p class="website">www.harlowfamilydentistry.com</p>

    <div class="base-stripe" aria-hidden="true"></div>
  </section>
</body>
</html>
```